Communication Business Card Design

We offer complete cabling solutions
Data Cabling,Fibre Optic, and Cabling Repairs fault finding
Security camera installation
TV Aerial installation
Security alarm installation
HWR

Industry/Entity Type

Business

Contact Information for Business Card

Brightmoor Solutions
ABN 58 214 992 367
EMAIL brightmoorsolutions.com.au
Mobile 0491236057
Lou Archer

```html
<!DOCTYPE html>
<html lang="en">
<head>
<meta charset="utf-8">
<title>Brightmoor Solutions – Business Cards</title>
<link href="https://fonts.googleapis.com/css2?family=Tinos&family=Open+Sans:wght@400&display=swap" rel="stylesheet">
<style>
  :root{
    --page:#e9e6e1;
    --navy-deep:#05081c;
    --navy:#141a5a;
    --navy-glow:#2a2f8f;
    --black:#0b0b0c;
    --charcoal:#202124;
    --silver:#c9cbcf;
    --silver-dark:#7d8085;
    --white:#ffffff;
    --blue-photo:#1b6fc4;
    --blue-photo-dark:#0a2a63;
    --teal-photo:#2f6e8a;
    --violet-photo:#3a3a8c;
  }
  *{box-sizing:border-box;margin:0;padding:0}
  html,body{width:1200px;height:892px;overflow:hidden;background:var(--page)}
  .sheet{position:relative;width:1200px;height:892px}
  .card{position:absolute;width:640px;height:391px;overflow:hidden;box-shadow:0 6px 18px rgba(0,0,0,.25)}

  /* services card */
  .card--services{left:280px;top:30px;
    background:radial-gradient(ellipse at 65% 55%,var(--navy-glow) 0%,var(--navy) 40%,var(--navy-deep) 85%);}
  .cable-art{position:absolute;left:150px;top:0;width:490px;height:300px;
    background:radial-gradient(ellipse at 40% 65%,rgba(210,220,235,.55) 0%,rgba(70,110,200,.35) 35%,rgba(20,26,90,0) 70%);}
  .card--services .brand{position:absolute;right:36px;top:40px;font-family:"Tinos",serif;
    color:var(--white);font-size:40px;letter-spacing:1px;text-transform:uppercase;}
  .services{position:absolute;left:40px;bottom:34px;right:30px;font-family:"Open Sans",sans-serif;
    color:var(--white);font-size:17px;line-height:1.6;list-style:none}
  .services li{display:inline}
  .services li::before{content:"\2022\00a0";}
  .services .row{display:block}

  /* contact card */
  .card--contact{left:280px;top:461px;background:var(--black)}
  .photo{position:absolute;top:0;height:240px}
  .photo--network{left:0;width:320px;
    background:radial-gradient(circle at 60% 55%,var(--blue-photo) 0%,var(--blue-photo-dark) 75%);}
  .photo--keyboard{left:320px;width:320px;
    background:linear-gradient(135deg,var(--teal-photo) 0%,var(--violet-photo) 60%,#1a1d4a 100%);}
  .swoosh{position:absolute;left:0;top:0;width:640px;height:391px}
  .card--contact .brand{position:absolute;left:0;right:0;top:36px;text-align:center;font-family:"Tinos",serif;
    color:var(--white);font-size:40px;letter-spacing:1px;text-transform:uppercase;text-shadow:0 2px 4px rgba(0,0,0,.5)}
  .person{position:absolute;left:60px;top:250px;font-family:"Tinos",serif;color:var(--white);font-size:34px}
  .divider{position:absolute;left:300px;top:230px;width:1px;height:120px;background:var(--silver-dark)}
  .contact{position:absolute;left:330px;top:248px;font-family:"Tinos",serif;color:var(--white);font-size:21px;line-height:1.55;list-style:none}
  .contact li{display:flex;align-items:center;gap:12px}
  .contact svg{width:16px;height:16px;flex:none}
  .contact .abn{padding-left:0}
</style>
</head>
<body>
<main class="sheet">

  <section class="card card--services">
    <div class="cable-art" role="img" aria-label="Cut fibre optic cable with coloured cores and glowing blue light strands"></div>
    <h2 class="brand">Brightmoor Solutions</h2>
    <ul class="services">
      <span class="row"><li>Security alarm installation</li></span>
      <span class="row"><li>TV Aerial installation</li> <li>Security camera installation</li></span>
      <span class="row"><li>Data Cabling,Fibre Optic, and Cabling Repairs fault finding</li> <li>HWR</li></span>
    </ul>
  </section>

  <section class="card card--contact">
    <div class="photo photo--network" role="img" aria-label="Network cables and plugs over a glowing blue digital background"></div>
    <div class="photo photo--keyboard" role="img" aria-label="Keyboard keys and a yellow network cable with fibre light sparkles"></div>
    <svg class="swoosh" viewBox="0 0 640 391" aria-hidden="true">
      <defs>
        <linearGradient id="silverBand" x1="0" y1="0" x2="1" y2="0">
          <stop offset="0" stop-color="#8e9196"/>
          <stop offset=".5" stop-color="#e4e5e8"/>
          <stop offset="1" stop-color="#9a9da2"/>
        </linearGradient>
        <linearGradient id="blackFill" x1="0" y1="0" x2="0" y2="1">
          <stop offset="0" stop-color="#242528"/>
          <stop offset="1" stop-color="#070708"/>
        </linearGradient>
      </defs>
      <path d="M0 130 C150 150 250 210 380 190 C480 175 560 190 640 250 L640 391 L0 391 Z" fill="url(#silverBand)"/>
      <path d="M0 142 C150 165 250 222 380 204 C480 190 560 205 640 262 L640 391 L0 391 Z" fill="url(#blackFill)"/>
    </svg>
    <h2 class="brand">Brightmoor Solutions</h2>
    <p class="person">Lou Archer</p>
    <div class="divider"></div>
    <ul class="contact">
      <li><svg viewBox="0 0 16 16" aria-hidden="true"><rect width="16" height="16" rx="2" fill="#fff"/><path d="M5 3.5l2 2-1.2 1.3c.6 1.4 1.6 2.4 3 3l1.3-1.2 2 2-1.2 1.6c-3.6-.4-6.6-3.4-7-7z" fill="#000"/></svg>0491236057</li>
      <li><svg viewBox="0 0 16 16" aria-hidden="true"><rect width="16" height="16" rx="2" fill="#fff"/><rect x="3" y="4" width="10" height="7" fill="#000"/><rect x="2" y="11.5" width="12" height="1.5" fill="#000"/></svg>brightmoorsolutions.com.au</li>
      <li class="abn">ABN 58 214 992 367</li>
    </ul>
  </section>

</main>
</body>
</html>
```